Hi,
We are an accounting firm looking to upgrade the following:
Logo, letterhead, withcomp slips and maybe our business cards. I have attached our original letterhead (sample A) and a letterhead (SAmple B) which we like the design and layout, however I want to stick with the colours of our orginal letterhead (Sample A) but improve and modernise the look with other letter head (Sample B) I have attached both. On the footer of Sample A, we would like to remove the names of the directors but leave EST. 1985 we also want to add the QRT logo ABN and TAX AGENT logo as stated in Sample B , we would like to do a layout for the header similar to SAmple B however maybe a bit more structured.

```html
<!DOCTYPE html>
<html lang="en">
<head>
<meta charset="utf-8">
<title>Brentholm Accountants – Stationery</title>
<link href="https://fonts.googleapis.com/css2?family=Montserrat:wght@400;500;600;700&display=swap" rel="stylesheet">
<style>
:root{
  --navy:#163a6b;
  --navy-deep:#122f55;
  --blue:#3a86c8;
  --ink:#4a4f57;
  --muted:#8a8f98;
  --paper:#ffffff;
  --bg:#e6e6e8;
  --bg-dark:#2b2b2d;
  --bar1:#e4e4e8;
  --bar2:#e7e7ee;
  --bar3:#edf1f8;
  --rule:#d9dbe0;
  --spiral:#3d3f44;
  --gold:#c9b233;
}
*{margin:0;padding:0;box-sizing:border-box}
html,body{width:1200px;height:3805px;overflow:hidden}
body{background:var(--bg);font-family:'Montserrat',sans-serif;color:var(--ink);position:relative}
.section{position:absolute;left:0;width:1200px}
.sheet{position:absolute;background:var(--paper);box-shadow:0 6px 18px rgba(0,0,0,.12);overflow:hidden}
.logo{display:flex;align-items:center;gap:6px;color:var(--navy);font-weight:600;line-height:1;white-space:nowrap}
.logo .mark{width:.55em;height:.55em;background:var(--navy);flex:none}
.logo.white{color:#fff}
.logo.white .mark{background:#fff}
.wave{position:absolute;left:0;bottom:0;width:100%;display:block}
.bar{position:absolute;bottom:0}

/* Sections */
.sec-letter{top:0;height:740px}
.sec-envelope{top:740px;height:805px}
.sec-notepad{top:1545px;height:710px}
.sec-comp{top:2255px;height:500px}
.sec-cards{top:2755px;height:1050px;background:var(--bg-dark)}

/* Letterhead */
.letterhead{left:380px;top:60px;width:440px;height:622px;font-size:6.2px;line-height:1.5}
.letterhead .logo{position:absolute;left:34px;top:34px;font-size:22px}
.lh-contact{position:absolute;left:196px;top:36px}
.lh-contact li{list-style:none;display:flex;gap:4px;align-items:center}
.lh-contact .dot{width:4px;height:4px;background:var(--navy);border-radius:50%}
.lh-company{position:absolute;right:30px;top:36px;text-align:right}
.lh-company b{color:var(--navy);font-weight:600}
.lh-recipient{position:absolute;left:34px;top:120px}
.lh-body{position:absolute;left:34px;top:180px;width:372px}
.lh-body p{margin-bottom:8px}
.lh-sign-line{position:absolute;left:34px;top:330px;width:80px;border-bottom:1px solid var(--ink)}
.lh-signoff{position:absolute;left:34px;top:340px}
.lh-footer{position:absolute;left:34px;bottom:56px;color:var(--muted)}
.lh-badges{position:absolute;right:30px;bottom:56px;display:flex;gap:8px;align-items:center}
.badge{width:18px;height:14px;background:var(--navy)}
.badge.alt{background:var(--blue)}
.badge.round{border-radius:50%;background:var(--gold);width:14px}

/* Envelope */
.envelope{top:270px;width:540px;height:270px}
.env-front{left:40px}
.env-back{left:620px}
.env-front .logo{position:absolute;left:30px;top:30px;font-size:24px}
.env-address{position:absolute;left:30px;top:64px;font-size:10px;line-height:1.4}
.env-address b{color:var(--navy);font-weight:500}
.env-flap{position:absolute;left:0;top:0;width:100%;height:64px;background:var(--navy-deep)}
.env-back .logo{position:absolute;right:30px;top:20px;font-size:24px}

/* Notepad */
.notepad{top:58px;width:364px;height:543px;border-radius:0 0 14px 14px;overflow:visible}
.pad-cover{left:204px;background:var(--navy)}
.pad-page{left:621px}
.spiral{position:absolute;top:-14px;left:20px;right:20px;height:22px;display:flex;justify-content:space-between}
.spiral span{width:3px;height:22px;background:var(--spiral);border-radius:2px}
.pad-cover .logo{position:absolute;left:0;right:0;top:240px;justify-content:center;font-size:44px}
.pad-page .logo{position:absolute;left:0;right:0;top:40px;justify-content:center;font-size:26px}
.pad-lines{position:absolute;left:36px;right:36px;top:96px}
.pad-lines div{height:26px;border-bottom:1px dashed var(--rule)}

/* Compliments slip */
.comp{left:242px;top:51px;width:714px;height:354px}
.comp .logo{position:absolute;left:55px;top:50px;font-size:34px}
.comp-title{position:absolute;right:50px;top:66px;font-size:20px;font-weight:500;color:var(--navy)}
.comp-title span{color:var(--blue)}
.comp-address{position:absolute;left:55px;top:222px;font-size:12.5px;line-height:1.3}
.comp-address b{color:var(--navy);font-weight:500}

/* Business cards */
.card{top:360px;width:500px;height:280px;border-radius:14px}
.card-back{left:60px;background:linear-gradient(135deg,#1c2f6e,#3a4c94 50%,#1c2f6e)}
.card-back .logo{position:absolute;right:36px;bottom:40px;font-size:30px}
.card-front{left:640px}
.card-front .logo{position:absolute;right:36px;top:34px;font-size:30px}
.card-rule{position:absolute;left:36px;right:36px;top:110px;border-top:1px solid var(--blue)}
.card-person{position:absolute;left:36px;top:128px;font-size:12px;line-height:1.4}
.card-person .name{color:var(--navy);font-weight:700;font-size:14px}
.card-person .role{color:var(--blue);font-weight:500;margin-bottom:6px}
.card-person li{list-style:none;display:flex;gap:6px;align-items:center;font-size:10.5px}
.card-person svg{width:10px;height:10px;fill:var(--navy);flex:none}
.card-company{position:absolute;right:36px;top:132px;text-align:right;font-size:10.5px;line-height:1.4}
</style>
</head>
<body>

<section class="section sec-letter">
  <article class="sheet letterhead">
    <div class="logo"><span class="mark"></span>Brentholm</div>
    <ul class="lh-contact">
      <li><span class="dot"></span>+61 3 9000 1234</li>
      <li><span class="dot"></span>+61 3 9000 5678</li>
      <li><span class="dot"></span>info@brentholm.com.au</li>
      <li><span class="dot"></span>www.brentholmaccountants.com.au</li>
    </ul>
    <div class="lh-company"><b>Brentholm Pty Ltd</b><br>ABN 00 000 000 000<br>27 Example Road<br>Northvale, Vic. 3000</div>
    <div class="lh-recipient">Recipient Name<br>Company Name<br>Street Address<br>Town, Post Code</div>
    <div class="lh-body">
      <p>Dear Client,</p>
      <p>Thank you for choosing our firm to look after your accounts this year. We have reviewed the documents you sent and prepared a short summary of the next steps. Please read the notes below and contact our office with any questions you may have.</p>
      <p>Our team will finalise your return once the remaining statements arrive. We aim to lodge within two weeks and will confirm each stage by email. We appreciate your trust and look forward to working with you again.</p>
      <p>Sincerely,</p>
    </div>
    <div class="lh-sign-line"></div>
    <div class="lh-signoff">Full Name<br>Director</div>
    <div class="lh-footer">Est. 1985<br>Registered Tax Agent</div>
    <div class="lh-badges"><span class="badge"></span><span class="badge alt"></span><span class="badge round"></span></div>
    <svg class="wave" viewBox="0 0 440 40" height="40" preserveAspectRatio="none">
      <path d="M0 14 Q220 4 440 22 L440 40 L0 40Z" fill="var(--navy-deep)"/>
      <path d="M0 10 Q220 -2 440 18" stroke="var(--blue)" stroke-width="3" fill="none"/>
    </svg>
  </article>
</section>

<section class="section sec-envelope">
  <article class="sheet envelope env-front">
    <div class="logo"><span class="mark"></span>Brentholm</div>
    <div class="env-address"><b>Brentholm Pty Ltd</b><br>27 Example Road<br>Northvale, Vic. 3000</div>
    <div class="bar" style="left:250px;width:70px;height:120px;background:var(--bar1)"></div>
    <div class="bar" style="left:340px;width:70px;height:150px;background:var(--bar2)"></div>
    <div class="bar" style="left:430px;width:70px;height:180px;background:var(--bar3)"></div>
    <svg class="wave" viewBox="0 0 540 270" height="270" preserveAspectRatio="none">
      <path d="M0 120 Q300 150 540 270 L460 270 Q280 170 0 128Z" fill="var(--navy-deep)"/>
      <path d="M0 112 Q300 140 540 262" stroke="var(--blue)" stroke-width="3" fill="none"/>
    </svg>
  </article>
  <article class="sheet envelope env-back">
    <div class="env-flap"></div>
    <div class="logo white"><span class="mark"></span>Brentholm</div>
  </article>
</section>

<section class="section sec-notepad">
  <article class="sheet notepad pad-cover">
    <div class="spiral"><span></span><span></span><span></span><span></span><span></span><span></span><span></span><span></span><span></span><span></span><span></span><span></span><span></span><span></span><span></span><span></span></div>
    <div class="logo white"><span class="mark"></span>Brentholm</div>
  </article>
  <article class="sheet notepad pad-page">
    <div class="spiral"><span></span><span></span><span></span><span></span><span></span><span></span><span></span><span></span><span></span><span></span><span></span><span></span><span></span><span></span><span></span><span></span></div>
    <div class="logo"><span class="mark"></span>Brentholm</div>
    <div class="pad-lines"><div></div><div></div><div></div><div></div><div></div><div></div><div></div><div></div><div></div><div></div><div></div><div></div><div></div><div></div><div></div><div></div></div>
  </article>
</section>

<section class="section sec-comp">
  <article class="sheet comp">
    <div class="logo"><span class="mark"></span>Brentholm</div>
    <div class="comp-title">WITH <span>COMPLIMENTS</span></div>
    <div class="bar" style="left:365px;width:95px;height:190px;background:var(--bar1)"></div>
    <div class="bar" style="left:492px;width:95px;height:225px;background:var(--bar2)"></div>
    <div class="bar" style="left:620px;width:95px;height:260px;background:var(--bar3)"></div>
    <div class="comp-address"><b>Brentholm Pty Ltd</b><br>ABN 00 000 000 000<br>27 Example Road<br>Northvale, Vic. 3000</div>
    <svg class="wave" viewBox="0 0 714 60" height="60" preserveAspectRatio="none">
      <path d="M0 40 Q300 10 714 24 L714 60 L0 60Z" fill="var(--navy-deep)"/>
      <path d="M0 36 Q260 6 540 14" stroke="var(--blue)" stroke-width="4" fill="none"/>
    </svg>
  </article>
</section>

<section class="section sec-cards">
  <article class="sheet card card-back" role="img" aria-label="Navy card back with a repeating pattern of small blue bars">
    <div class="logo white"><span class="mark"></span>Brentholm</div>
  </article>
  <article class="sheet card card-front">
    <div class="logo"><span class="mark"></span>Brentholm</div>
    <div class="card-rule"></div>
    <div class="card-person">
      <div class="name">HARLAN MERCER</div>
      <div class="role">Managing Director</div>
      <ul>
        <li><svg viewBox="0 0 10 10"><path d="M2 0h2l1 3-1.5 1a6 6 0 0 0 2.5 2.5L7 5l3 1v2a2 2 0 0 1-2 2A8 8 0 0 1 0 2a2 2 0 0 1 2-2z"/></svg>+61 3 9000 1234</li>
        <li><svg viewBox="0 0 10 10"><rect x="0" y="2" width="10" height="7" rx="1"/></svg>+61 3 9000 5678</li>
        <li><svg viewBox="0 0 10 10"><path d="M0 2h10v6H0z"/></svg>info@brentholm.com.au</li>
        <li><svg viewBox="0 0 10 10"><circle cx="5" cy="5" r="5"/></svg>www.brentholmaccountants.com.au</li>
      </ul>
    </div>
    <div class="card-company">Brentholm Pty Ltd<br>ABN 00 000 000 000<br>27 Example Road<br>Northvale, Vic. 3000</div>
    <svg class="wave" viewBox="0 0 500 50" height="50" preserveAspectRatio="none">
      <path d="M0 46 Q260 30 500 4 L500 50 L0 50Z" fill="var(--navy-deep)"/>
      <path d="M0 40 Q260 24 500 0" stroke="var(--blue)" stroke-width="3" fill="none"/>
    </svg>
  </article>
</section>

</body>
</html>
```